!st birthday celebration

Im looking for a celebration type of flyer for our first birthday. something colorful and eye catching but with a vintage feel to it. we are a vintage shop with a friendly atmosphere and always have music playing. I have attached a draft copy i have been working on so far. Thanks

Industry/Entity Type

Shop

```html
<!DOCTYPE html>
<html lang="en">
<head>
<meta charset="utf-8">
<title>Otter Vintage – 1st Birthday Flyer</title>
<link rel="stylesheet" href="https://fonts.googleapis.com/css2?family=Alfa+Slab+One&family=Yellowtail&family=Reenie+Beanie&family=Special+Elite&family=Kaushan+Script&display=swap">
<style>
  :root {
    --canvas: #ffffff;
    --wine: #7e2a2a;
    --wine-deep: #5e1a1c;
    --wine-band: #6a1f22;
    --rose: #c9666e;
    --rose-pale: #d98a8f;
    --paper: #ece2d8;
    --cream: #f3efc6;
    --gold: #f1dc4a;
    --gold-bright: #ffe94d;
    --orange: #e8892f;
    --teal: #86e6d4;
    --pink: #f6b9e8;
    --periwinkle: #7c8ae6;
    --peach: #f6a866;
    --sand: #f2dc98;
    --ink-red: #c23a3c;
    --ink-wine: #7a2326;
    --chevron: #8e5d48;
    --label: #7a1f1f;
  }
  * { margin: 0; padding: 0; box-sizing: border-box; }
  html, body { width: 1200px; height: 870px; overflow: hidden; background: var(--canvas); }
  .sheet { position: relative; width: 1200px; height: 870px; }
  .flyer { position: absolute; top: 0; width: 584px; height: 828px; }
  .flyer--front { left: 8px; }
  .flyer--back { left: 608px; width: 580px; }
  .flyer svg { display: block; }
  .side-label {
    position: absolute; top: 832px;
    font-family: Arial, Helvetica, sans-serif;
    font-size: 32px; color: var(--label); letter-spacing: 0.5px;
  }
  .side-label--front { left: 10px; }
  .side-label--back { left: 608px; }
  .brand-name { font-family: 'Kaushan Script', cursive; font-size: 44px; fill: var(--cream); }
  .tagline { font-family: 'Kaushan Script', cursive; font-size: 17px; fill: var(--cream); }
  .headline { font-family: 'Yellowtail', 'Kaushan Script', cursive; fill: var(--gold); }
  .headline-accent { fill: var(--gold-bright); }
  .band-title { font-family: 'Alfa Slab One', serif; font-size: 84px; fill: var(--cream); }
  .invite { font-family: 'Reenie Beanie', cursive; font-size: 36px; fill: var(--ink-wine); }
  .event-detail { font-family: 'Alfa Slab One', serif; font-size: 21px; fill: var(--ink-red); letter-spacing: 1px; }
  .intro-script { font-family: 'Yellowtail', 'Kaushan Script', cursive; font-size: 48px; fill: var(--sand); }
  .feature { font-family: 'Alfa Slab One', serif; }
  .contact { font-family: 'Special Elite', 'Courier New', monospace; font-size: 17px; fill: var(--sand); }
</style>
</head>
<body>
<main class="sheet">

  <section class="flyer flyer--front" aria-label="Flyer front">
    <svg width="584" height="828" viewBox="0 0 584 828">
      <rect class="front-ground" width="584" height="828" fill="var(--wine)"/>

      <g class="brand">
        <rect x="118" y="78" width="16" height="16" fill="var(--gold)"/>
        <text class="brand-name" x="300" y="104" text-anchor="middle">Otter Vintage</text>
        <text class="tagline" x="292" y="182" text-anchor="middle">Vintage - Retro Clothing &amp; Collectables</text>
      </g>

      <rect class="splash-decor" role="img" aria-label="Orange and green paint splash ornaments framing the birthday heading"
            x="20" y="205" width="544" height="230" rx="110" fill="var(--orange)" opacity="0.28"/>

      <g class="birthday-heading" transform="rotate(-4 292 320)">
        <text class="headline" x="178" y="300" font-size="92" text-anchor="middle">Happy</text>
        <text class="headline headline-accent" x="410" y="300" font-size="104" text-anchor="middle">1st</text>
        <text class="headline" x="300" y="400" font-size="100" text-anchor="middle">Birthday</text>
      </g>

      <g class="name-band">
        <polygon points="0,478 584,398 584,545 0,628" fill="var(--wine-band)"/>
        <polygon points="0,628 584,545 584,575 0,660" fill="var(--rose)"/>
        <polygon points="0,660 584,575 584,590 0,676" fill="var(--rose-pale)" opacity="0.7"/>
        <line x1="0" y1="488" x2="584" y2="408" stroke="var(--cream)" stroke-width="4" stroke-dasharray="3 6"/>
        <line x1="0" y1="617" x2="584" y2="535" stroke="var(--cream)" stroke-width="4" stroke-dasharray="3 6"/>
        <text class="band-title" x="292" y="548" text-anchor="middle" textLength="560" lengthAdjust="spacingAndGlyphs"
              transform="rotate(-8 292 520)" stroke="var(--wine-deep)" stroke-width="2">OTTER VINTAGE</text>
      </g>

      <polygon class="invite-panel" points="0,676 584,590 584,828 0,828" fill="var(--paper)"/>

      <g class="invitation">
        <text class="invite" x="565" y="672" text-anchor="end">You are invited to help</text>
        <text class="invite" x="568" y="718" text-anchor="end">celebrate in the festivities!</text>
        <text class="event-detail" x="558" y="760" text-anchor="end">DATE: 19TH&amp; 20TH JULY</text>
        <text class="event-detail" x="558" y="796" text-anchor="end">FROM 11:00AM ONWARDS</text>
      </g>

      <g class="chevrons" fill="var(--chevron)">
        <polygon points="20,742 52,742 76,772 52,802 20,802 44,772"/>
        <polygon points="66,742 98,742 122,772 98,802 66,802 90,772"/>
        <polygon points="112,742 144,742 168,772 144,802 112,802 136,772"/>
        <polygon points="158,742 190,742 214,772 190,802 158,802 182,772"/>
      </g>
    </svg>
  </section>

  <section class="flyer flyer--back" aria-label="Flyer back">
    <svg width="580" height="828" viewBox="0 0 580 828">
      <rect class="back-ground" width="580" height="828" fill="var(--wine)"/>
      <rect class="back-frame" x="14" y="14" width="552" height="800" rx="22" fill="none"
            stroke="var(--sand)" stroke-width="4" stroke-dasharray="2 7" opacity="0.8"/>

      <g class="feature-list" transform="rotate(-6 290 400)">
        <text class="intro-script" x="290" y="150" text-anchor="middle" textLength="460" lengthAdjust="spacingAndGlyphs">festivities will include:</text>

        <g class="dividers" stroke="var(--teal)" stroke-width="4" stroke-dasharray="3 6" fill="none">
          <line x1="70" y1="172" x2="510" y2="172"/>
          <line x1="70" y1="226" x2="510" y2="226"/>
          <line x1="70" y1="296" x2="510" y2="296"/>
          <line x1="70" y1="386" x2="510" y2="386"/>
          <line x1="70" y1="468" x2="510" y2="468"/>
          <line x1="70" y1="564" x2="510" y2="564"/>
          <line x1="70" y1="650" x2="510" y2="650"/>
        </g>

        <text class="feature" x="290" y="214" text-anchor="middle" font-size="40" fill="var(--teal)"
              textLength="440" lengthAdjust="spacingAndGlyphs">POP UP MARKET STALLS</text>
        <text class="feature" x="290" y="282" text-anchor="middle" font-size="52" fill="var(--gold)"
              textLength="460" lengthAdjust="spacingAndGlyphs">BEST DRESSED VINTAGE OUTFIT</text>
        <text class="feature" x="290" y="370" text-anchor="middle" font-size="66" fill="var(--pink)"
              textLength="450" lengthAdjust="spacingAndGlyphs">FACE PAINTING</text>
        <text class="feature" x="290" y="452" text-anchor="middle" font-size="54" fill="var(--teal)"
              textLength="460" lengthAdjust="spacingAndGlyphs">VINTAGE CARS ON DISPLAY</text>
        <text class="feature" x="290" y="548" text-anchor="middle" font-size="76" fill="var(--periwinkle)"
              textLength="330" lengthAdjust="spacing">MUSIC</text>
        <text class="feature" x="290" y="634" text-anchor="middle" font-size="64" fill="var(--peach)"
              textLength="460" lengthAdjust="spacingAndGlyphs">REFRESHMENTS</text>
      </g>

      <g class="contact-block">
        <text class="contact" x="290" y="728" text-anchor="middle">82 HARBOUR VIEW RD, ELMSFORD</text>
        <text class="contact" x="290" y="758" text-anchor="middle">PH: 59 010....</text>
        <text class="contact" x="290" y="788" text-anchor="middle">MOBILE: 0400123456</text>
      </g>
    </svg>
  </section>

  <p class="side-label side-label--front">FRONT</p>
  <p class="side-label side-label--back">BACK</p>
</main>
</body>
</html>
```